4 Color TRI-Fold Real Estate Promotional Brochure

8.5"x11" tri-fold brochure for printing. full color with photos per upload. You have full creative license regarding the design. The design include both front and back. This is a marketing piece and should be "eye catching". The blues should be deep as well as the red. Do not use garish colors. Clear concise fonts would be best.

Target Market(s)

Buyers of Caribbean properties such as investors and retirees

Industry/Entity Type

Real Estate

Font styles to use
Serif
Script

Colors
0455a3
ec1f27

Requirements
Must have
• Company name and logo. All property photos. Location map. Agent information.
Should not have
• garish colors

```html
<!DOCTYPE html>
<html lang="en">
<head>
<meta charset="utf-8">
<title>Seagrape House Bequia – Tri-fold Brochure</title>
<link rel="stylesheet" href="https://fonts.googleapis.com/css2?family=Jost:wght@400;500;600&family=Lobster&display=swap">
<style>
  :root {
    --brand-blue: #0455a3;
    --brand-red: #ec1f27;
    --paper-grey: #e9e9eb;
    --page-bg: #d9d9d9;
    --white: #ffffff;
    --sea: #4f88b8;
    --sky: #9cc4e2;
    --pool: #3fc3c0;
    --foliage: #5f8a3a;
    --wood: #8a5a35;
  }
  * { box-sizing: border-box; margin: 0; padding: 0; }
  html, body { width: 1200px; height: 816px; overflow: hidden; }
  body {
    background: var(--page-bg);
    font-family: "Jost", "Futura", sans-serif;
    position: relative;
  }
  .brochure {
    position: absolute;
    left: 100px; top: 22px;
    width: 1000px; height: 772px;
    display: flex;
    box-shadow: 0 6px 24px rgba(0,0,0,.18);
  }
  .panel {
    position: relative;
    width: 333.33px; height: 100%;
    overflow: hidden;
  }
  .panel + .panel { border-left: 1px solid rgba(0,0,0,.08); }
  .panel svg.shapes { position: absolute; inset: 0; width: 100%; height: 100%; }
  .photo { position: absolute; }
  .photo-round {
    position: absolute;
    border-radius: 50%;
    border: 4px solid var(--brand-red);
  }
  .photo-round.light-ring { border-color: #dfe6ef; }
  .script-heading {
    font-family: "Lobster", cursive;
    font-weight: 400;
    line-height: 1.05;
  }
  .copy {
    position: absolute;
    font-size: 10.4px;
    line-height: 1.45;
    text-align: justify;
  }
  .copy p + p { margin-top: 10px; }
  .on-blue { color: var(--white); }
  .on-grey { color: #1f2b4a; }

  /* Left panel */
  .mustique-title { position: absolute; left: 22px; top: 372px; font-size: 22px; color: var(--white); }
  .mustique-copy { left: 22px; top: 402px; width: 292px; }
  .villa-title {
    position: absolute; left: 22px; top: 482px; width: 292px;
    text-align: center; color: var(--white);
    font-size: 13.5px; font-weight: 500; letter-spacing: .6px;
  }
  .villa-subtitle { position: absolute; left: 22px; top: 501px; width: 292px; text-align: right; font-size: 14px; color: var(--white); }
  .villa-copy { left: 22px; top: 528px; width: 292px; }

  /* Middle panel */
  .description-title {
    position: absolute; right: 26px; top: 222px;
    text-align: center; font-size: 22px; color: var(--brand-red);
  }
  .description-copy { left: 20px; top: 284px; width: 294px; }

  /* Right panel */
  .location-title { position: absolute; right: 20px; top: 36px; text-align: right; font-size: 17px; color: var(--white); }
  .location-copy { left: 20px; top: 86px; width: 294px; }
  .agency-note {
    position: absolute; left: 20px; top: 326px; width: 294px;
    background: var(--brand-red); color: var(--white);
    font-size: 8.4px; line-height: 1.4; padding: 6px 8px;
  }
</style>
</head>
<body>
<main class="brochure">

  <section class="panel panel-intro">
    <div class="photo" role="img" aria-label="Photo of a sailboat anchored in a calm bay framed by palm trees"
         style="left:0;top:0;width:100%;height:360px;background:linear-gradient(180deg,var(--sky) 0%,var(--sea) 45%,#3c6f9b 70%,#6d8b5a 100%);"></div>
    <svg class="shapes" viewBox="0 0 333 772" preserveAspectRatio="none" aria-hidden="true">
      <path d="M0,358 C110,340 220,320 333,262 L333,772 L0,772Z" fill="var(--brand-blue)"/>
      <path d="M0,358 C110,340 220,320 333,262" fill="none" stroke="var(--brand-red)" stroke-width="6"/>
    </svg>
    <div class="photo-round" role="img" aria-label="Photo of a canopy bed in a bright bedroom"
         style="left:196px;top:150px;width:92px;height:92px;background:radial-gradient(circle,#f4e6c4,#b08b5c);"></div>
    <div class="photo" role="img" aria-label="Photo of a stone terrace at the villa"
         style="left:180px;top:640px;width:160px;height:140px;clip-path:polygon(100% 0,100% 100%,0 100%);background:linear-gradient(135deg,#4a4a3e,#2a2a24);"></div>
    <div class="photo-round light-ring" role="img" aria-label="Photo of the villa living room with wooden furniture"
         style="left:40px;top:650px;width:112px;height:112px;background:radial-gradient(circle,#c9a27a,var(--wood));"></div>

    <h2 class="script-heading mustique-title">Mustique</h2>
    <div class="copy on-blue mustique-copy">
      <p>Beautiful white sand beaches and a gentle terrain, Mustique is smaller than St. Vincent, just under five square miles. A unique, private island with exclusive villas, and opulent architectural beauties on dramatic hilltops. Mustique is home to not only the rich and famous but also royalty.</p>
    </div>
    <h1 class="villa-title">SEAGRAPE HOUSE BEQUIA</h1>
    <p class="script-heading villa-subtitle">St. Vincent &amp; The Grenadines</p>
    <div class="copy on-blue villa-copy">
      <p>Fulfill your dream of enjoying the beauty and relaxed lifestyle of the Caribbean. This lovely 4000 sq.ft. villa is ideally located on the tiny Caribbean island of Bequia in the Grenadines. Perfect for year round living, vacation get-away, a retirement property with rental income or simply as an investment. Located just steps from the beach, and short distance to boutique hotels, shopping, bars and restaurants.</p>
    </div>
  </section>

  <section class="panel panel-description">
    <div class="photo" role="img" aria-label="Photo of the villa pool surrounded by palms"
         style="left:0;top:0;width:100%;height:240px;background:linear-gradient(180deg,#2f4a2c 0%,#5c7a45 30%,var(--pool) 60%,#7fd8d0 100%);"></div>
    <div class="photo" role="img" aria-label="Photo of the villa courtyard, verandah and guest bedroom"
         style="left:0;top:480px;width:100%;height:292px;background:linear-gradient(180deg,#c9b79a 0%,#8a7a62 50%,#4e4a3e 100%);"></div>
    <svg class="shapes" viewBox="0 0 333 772" preserveAspectRatio="none" aria-hidden="true">
      <path d="M0,258 C120,250 230,230 333,190 L333,484 C230,512 120,534 0,574Z" fill="var(--paper-grey)"/>
      <path d="M0,258 C120,250 230,230 333,190" fill="none" stroke="var(--brand-red)" stroke-width="7"/>
      <path d="M333,484 C230,512 120,534 0,574" fill="none" stroke="var(--brand-red)" stroke-width="7"/>
    </svg>
    <div class="photo-round" role="img" aria-label="Photo of the covered outdoor dining area"
         style="left:8px;top:178px;width:92px;height:92px;background:radial-gradient(circle,#e8a35a,#7a4a2a);"></div>
    <div class="photo-round" role="img" aria-label="Photo of a guest bedroom with colourful bedding"
         style="left:10px;top:512px;width:86px;height:86px;background:radial-gradient(circle,#e9c9a0,#9a4a3a);"></div>

    <h2 class="script-heading description-title">Property<br>Description</h2>
    <div class="copy on-grey description-copy">
      <p>Built of natural stone and wood with vaulted wood beam ceilings, tile and wood flooring. It consists of 2 Buildings built around a central court yard with a pool and covered entertainment spaces. The main house has the master bedroom with an ensuite bath, an open living area, a spacious kitchen and private patio.</p>
      <p>The "cottage" across the courtyard boasts two bedrooms and bath, ideal for providing additional vacation rental income. Features include, air conditioning, ceiling fans, and internet access. A detached garage on this treed, 1/2 acre property could be converted into an apartment for your guests or additional vacation rental income. (Ask about current income from vacation bookings).</p>
    </div>
  </section>

  <section class="panel panel-location">
    <div class="photo" role="img" aria-label="Photo of the tropical garden path and yellow gate"
         style="left:0;top:400px;width:100%;height:372px;background:linear-gradient(160deg,#8fb46a 0%,var(--foliage) 45%,#d8b340 75%,#6e6a5a 100%);"></div>
    <svg class="shapes" viewBox="0 0 333 772" preserveAspectRatio="none" aria-hidden="true">
      <path d="M0,0 L333,0 L333,410 C220,428 110,456 0,484Z" fill="var(--brand-blue)"/>
      <path d="M333,410 C220,428 110,456 0,484" fill="none" stroke="var(--brand-red)" stroke-width="7"/>
    </svg>
    <div class="photo" role="img" aria-label="Photo of palm fronds over the pool edge"
         style="left:0;top:0;width:90px;height:70px;clip-path:polygon(0 0,100% 0,0 100%);background:linear-gradient(135deg,#2f4a2c,#5c7a45);"></div>

    <h2 class="script-heading location-title">Bequia, Saint Vincent<br>&amp; The Grenadines</h2>
    <div class="copy on-blue location-copy">
      <p>Not as well know as many of the Caribbean islands, this piece of paradise has been one of the preferred destinations of wealthy yachting enthusiasts. With all its' breathtaking scenery, exquisite powder beaches, turquoise waters, tropical warm weather and protected natural harbours.</p>
      <p>This gem in the necklace of Caribbean islands consists of 32 islands, 9 of which are inhabited. Bequia has a significant number of expats, an international community that is friendly and sociable. This truly unspoiled natural beauty offers it's visitors and residents a hosts of activities from sailing, hiking, swimming in waterfalls, exploring of underwater gardens, dolphin and whale watching and so much more. Affordable household help will give you the time to enjoy a lifestyle you have only dreamed of.</p>
    </div>
    <p class="agency-note">Buying property in the Caribbean can be challenging. HARBOURLINE REALTY is pleased to provide you with efficient, knowledgeable professional service. We also offer our property buyer clients a package of concierge services to make your visit and buying experience more enjoyable.</p>
  </section>

</main>
</body>
</html>
```